Empower our Electric Journey on the Web

We need a new website that can promote our services. Our three services that we offer are:
- Management of e-mobility charging stations
- Management of energy purchases
- Leasing of E-Mobility charging stations
- Energy billing of private electricity meters
The website should work responsively on PC, tablet and smartphone. In general, a simple navigation and an appealing design should be in the foreground. The website should give the customer the possibility to request , based pm a preset chexkbox chart and to get in contact with us.
Our logo works on black and white background.
Our slogan is:
Empower Your Electric Journey with Velnik Mobility
The 4 Pages should be the following:
Main Page, with info about us, why choose us,
2nd; services; what we sell and what are our services
3rd; Contact us, request an offer
4th, References about costumers and Work we already did, in the future we would like to integrate a Blog Post in this section in stead of references.

Target Market(s)

Landlords, Homeowners, Homeowner Associations

Industry/Entity Type

EV Chargers / E-Mobility

Coding

Coded - Design and coding required

Number of Pages Required

4 page

Requirements
Nice to have
• Pop up to our mailchimp newsletter subscription

```html
<!DOCTYPE html>
<html lang="en">
<head>
<meta charset="utf-8">
<title>Velnik Mobility</title>
<link href="https://fonts.googleapis.com/css2?family=Inter:wght@300;400;500;600&display=swap" rel="stylesheet">
<style>
:root{
  --ink:#101010;
  --green:#3fba43;
  --green-mid:#68cd43;
  --green-light:#85e943;
  --paper:#f1f2f3;
  --white:#ffffff;
  --grey:#6f7275;
  --line:#c9cbcd;
  --stage:#e6e6e6;
}
*{box-sizing:border-box;margin:0;padding:0}
html,body{width:1200px;height:4035px;overflow:hidden}
body{background:var(--stage);font-family:"Inter",Helvetica,Arial,sans-serif;color:var(--ink)}
.site{position:absolute;left:155px;top:0;width:890px;height:4035px;background:var(--white);overflow:hidden}
.abs{position:absolute}

/* hero */
.hero{position:absolute;left:0;top:0;width:890px;height:444px}
.hero-photo{position:absolute;inset:0;background:
  radial-gradient(ellipse at 40% 85%,#6d7470 0%,rgba(109,116,112,0) 45%),
  linear-gradient(180deg,#eef4e8 0%,#dfe7d8 38%,#a8b0a6 62%,#5f665f 100%)}
.brand{position:absolute;left:63px;top:16px;display:flex;align-items:center;gap:6px;font-size:11px;font-weight:600;color:var(--green);letter-spacing:.02em}
.brand i{width:9px;height:9px;background:var(--green);display:block}
.nav{position:absolute;top:18px;left:0;width:890px;font-size:8px;color:#3a3d3a}
.nav span{position:absolute}
.hero-title{position:absolute;top:98px;left:0;width:890px;text-align:center;font-size:36px;line-height:41px;font-weight:300;letter-spacing:-.01em}
.hero-title b{font-weight:600}
.btn-fill{position:absolute;left:400px;top:240px;width:90px;height:27px;border-radius:14px;background:var(--green-mid);color:#fff;font-size:7px;display:flex;align-items:center;justify-content:center}

/* features */
.feature{position:absolute;top:505px}
.feature h4{font-size:11px;font-weight:500;display:flex;align-items:center;gap:6px}
.feature h4 svg{display:block}
.feature p{font-size:7.5px;color:var(--grey);margin-top:8px}
.rule{position:absolute;left:63px;width:762px;height:1px;background:var(--line)}

/* intro */
.h2{position:absolute;font-size:29px;line-height:36px;font-weight:500;letter-spacing:-.01em}
.lead{position:absolute;font-size:13px;line-height:20px;color:#2a2c2d}
.small{position:absolute;font-size:8px;line-height:13px;color:var(--grey)}
.btn-line{position:absolute;height:25px;border:1px solid var(--green);border-radius:13px;font-size:7px;display:flex;align-items:center;justify-content:center}

/* dark band */
.dark{position:absolute;left:0;top:1044px;width:890px;height:797px;background:var(--ink);color:#fff}
.photo{position:absolute}
.dark .h2{color:#fff;font-size:28px;line-height:32px}
.dark .btn-line{color:#fff}

/* services */
.tabs{position:absolute;top:2018px;left:63px;width:762px;font-size:10.5px;line-height:14px;color:var(--grey)}
.tabs span{position:absolute}
.tabs .on{color:var(--ink)}
.tab-bar{position:absolute;left:63px;top:2061px;width:140px;height:3px;background:var(--green-mid)}

/* cases */
.case-date{position:absolute;font-size:7px;color:var(--grey)}
.case-title{position:absolute;font-size:14px;line-height:20px;color:#202223}

/* faq */
.faq{position:absolute;left:63px;width:358px;display:flex;justify-content:space-between;font-size:10px;color:#2a2c2d;padding-bottom:9px;border-bottom:1px solid var(--line)}
.ask{position:absolute;left:672px;top:3486px;font-size:18px;line-height:22px}
.ask a{color:var(--green);text-decoration:underline;text-decoration-thickness:1px}

/* footer */
.footer{position:absolute;left:0;top:3590px;width:890px;height:445px;background:var(--ink);color:#fff}
.f-label{position:absolute;font-size:7px;color:#8a8d90}
.f-list{position:absolute;font-size:11px;line-height:23px;list-style:none}
.f-brand{position:absolute;left:63px;top:250px;display:flex;align-items:center;gap:6px;font-size:12px;font-weight:600;color:var(--green)}
.f-brand i{width:9px;height:9px;background:var(--green);display:block}
.f-copy{position:absolute;left:63px;top:273px;font-size:6.5px;color:#b6b9bc}
.f-input{position:absolute;left:461px;top:270px;width:200px;height:30px;border-bottom:1px solid #6a6d70;font-size:10px;display:flex;align-items:center}
.f-send{position:absolute;left:664px;top:270px;width:33px;height:30px;background:var(--green);display:flex;align-items:center;justify-content:center}
.f-rule{position:absolute;left:0;top:356px;width:890px;height:1px;background:#2c2e30}
.f-legal{position:absolute;left:63px;top:386px;font-size:6.5px;line-height:11px;list-style:none}
.f-note{position:absolute;left:324px;top:386px;width:500px;font-size:6px;line-height:10px;color:#8a8d90}
</style>
</head>
<body>
<main class="site">

  <header class="hero">
    <div class="hero-photo" role="img" aria-label="Futuristic charging pavilion with a white electric car on a winding mountain road"></div>
    <div class="brand"><i></i>Velnik Mobility</div>
    <nav class="nav">
      <span style="left:511px">Home</span>
      <span style="left:576px">About Us</span>
      <span style="left:652px">Services</span>
      <span style="left:724px">Insights</span>
      <span style="left:797px">Contact</span>
    </nav>
    <h1 class="hero-title">Empower Your<br><b>Electric Journey</b><br>with Velnik Mobility</h1>
    <a class="btn-fill">Explore More</a>
  </header>

  <section>
    <div class="feature" style="left:63px"><h4><svg width="8" height="6"><path d="M0 6L8 0" stroke="#3fba43" stroke-width="1.6"/></svg>Expertise</h4><p>Electric Solutions for Everyone</p></div>
    <div class="feature" style="left:283px"><h4><svg width="8" height="6"><path d="M0 6L8 0" stroke="#3fba43" stroke-width="1.6"/></svg>Flexibility</h4><p>Scalability &amp; Future-Readiness</p></div>
    <div class="feature" style="left:502px"><h4><svg width="8" height="6"><path d="M0 6L8 0" stroke="#3fba43" stroke-width="1.6"/></svg>Affordability</h4><p>Cost-Effective Solutions</p></div>
    <div class="feature" style="left:695px"><h4><svg width="8" height="6"><path d="M0 6L8 0" stroke="#3fba43" stroke-width="1.6"/></svg>Custom Solutions</h4><p>Comprehensive Service Portfolio</p></div>
    <div class="rule" style="top:602px"></div>

    <h2 class="h2" style="left:63px;top:664px;width:440px">Elevate Your Vision with Cutting-Edge Solutions for E-Mobility Charging Station and Energy Management</h2>
    <p class="lead" style="left:187px;top:846px;width:265px">We are dedicated to pushing the boundaries of what's possible in the management of e-mobility charging</p>
    <p class="small" style="left:510px;top:846px;width:315px">In the midst of the e-mobility revolution, our company Velnik was the first to recognize the urgency of harnessing software solutions for secure and strategic decision-making.</p>
    <p class="small" style="left:510px;top:894px;width:315px">We understand that our clients are facing unprecedented disruption in the transportation sector and the need to adapt is existential.</p>
    <a class="btn-line" style="left:510px;top:954px;width:114px">Learn More About Velnik</a>
  </section>

  <section class="dark">
    <div class="photo" style="left:63px;top:63px;width:361px;height:468px;background:linear-gradient(135deg,#e9ece6 0%,#bfc4bd 45%,#5b5f5b 100%)" role="img" aria-label="Smiling advisor in a patterned blouse"></div>
    <h2 class="h2" style="left:510px;top:84px;width:330px">A Team of Reliable and Experienced Advisors</h2>
    <a class="btn-line" style="left:510px;top:178px;width:106px">Talk to an expert</a>
    <div class="photo" style="left:510px;top:250px;width:315px;height:466px;background:linear-gradient(180deg,#1b1c1c 0%,#1b1c1c 18%,#b9bcb4 30%,#8a8a7a 48%,#2b2c2b 70%,#141414 100%)" role="img" aria-label="Driver's hands on the wheel of an electric car in the mountains"></div>
    <h2 class="h2" style="left:63px;top:588px;width:380px">Got Any E-Mobility Idea? Submit Your Offer Today</h2>
    <a class="btn-line" style="left:63px;top:690px;width:106px">Make an Offer</a>
  </section>

  <section>
    <h2 class="h2" style="left:63px;top:1897px;width:420px">Unlocking a Vast Array of E-Mobility Services</h2>
    <div class="tabs">
      <span class="on" style="left:0">Management of e-mobility<br>charging stations</span>
      <span style="left:237px">Management of<br>energy purchases</span>
      <span style="left:430px">Leasing of E-Mobility<br>charging stations</span>
      <span style="left:637px">Energy billing of private<br>electricity meters</span>
    </div>
    <div class="tab-bar"></div>
    <div class="photo" style="left:63px;top:2086px;width:762px;height:366px;background:linear-gradient(110deg,#2c322c 0%,#58624f 30%,#c7cfc0 60%,#eef0ec 100%)" role="img" aria-label="Man plugging a wall charger cable into a white electric car"></div>
    <p class="lead" style="left:173px;top:2478px;width:265px">We handle all aspects of maintenance and repairs, reducing downtime and keeping your charging stations in peak condition.</p>
    <p class="small" style="left:528px;top:2478px;width:297px">Our e-mobility charging station management service offers seamless and efficient control of electric vehicle charging infrastructure. From monitoring and maintenance to user access and billing, we ensure that your charging stations are always ready for action.</p>
    <div class="rule" style="top:2628px"></div>
  </section>

  <section>
    <h2 class="h2" style="left:63px;top:2688px;width:420px">Case Studies/ Resources and Blog Insights</h2>
    <div class="photo" style="left:63px;top:2811px;width:357px;height:225px;background:linear-gradient(120deg,#d8dcd6 0%,#8d958a 45%,#4d5a3f 100%)" role="img" aria-label="Couple charging an electric car outside a modern house"></div>
    <span class="case-date" style="left:63px;top:3050px">09/16/23</span>
    <p class="case-title" style="left:63px;top:3066px;width:357px">A Comprehensive Guidance to Electric Vehicle Charging Infrastructure</p>
    <div class="photo" style="left:443px;top:2811px;width:192px;height:140px;background:linear-gradient(160deg,#cfd2cf 0%,#6f726f 40%,#1c1d1d 100%)" role="img" aria-label="Hand resting on the steering wheel of an electric car"></div>
    <span class="case-date" style="left:443px;top:2965px">09/16/23</span>
    <p class="case-title" style="left:443px;top:2981px;width:200px">Exploring High-End Electric Vehicle Options</p>
    <div class="photo" style="left:657px;top:2811px;width:168px;height:102px;background:linear-gradient(120deg,#4a4f45 0%,#8f9a6f 50%,#d4dc9a 100%)" role="img" aria-label="Woman charging a yellow-green electric car"></div>
    <span class="case-date" style="left:657px;top:2926px">09/16/23</span>
    <p class="case-title" style="left:657px;top:2942px;width:170px">Top EV Charging Tips</p>
    <div class="rule" style="top:3168px"></div>
  </section>

  <section>
    <h2 class="h2" style="left:63px;top:3226px;width:320px">Frequently Asked Questions</h2>
    <div class="faq" style="top:3345px"><span>How are private electricity meters billed in commercial settings?</span><span>+</span></div>
    <div class="faq" style="top:3387px"><span>How do you manage e-mobility charging stations efficiently?</span><span>+</span></div>
    <div class="faq" style="top:3430px"><span>Are there lease-to-own options for e-mobility charging stations?</span><span>+</span></div>
    <div class="faq" style="top:3472px"><span>What's the key to effective energy purchase management?</span><span>+</span></div>
    <div class="faq" style="top:3514px"><span>What are some tips for efficient energy purchase management?</span><span>+</span></div>
    <p class="ask">Got any question?<br>Send it <a>here</a></p>
  </section>

  <footer class="footer">
    <span class="f-label" style="left:324px;top:66px">About</span>
    <ul class="f-list" style="left:324px;top:82px"><li>Company</li><li style="margin-top:-4px">Mission</li><li style="margin-top:-4px">Make Offer</li></ul>
    <span class="f-label" style="left:461px;top:66px">Services</span>
    <ul class="f-list" style="left:461px;top:82px"><li>Management of E-mobility charging stations</li><li>Management of energy purchases</li><li>Leasing of E-Mobility charging stations</li><li>Energy billing of private electricity meters</li></ul>
    <span class="f-label" style="left:773px;top:66px">Resources</span>
    <ul class="f-list" style="left:773px;top:82px"><li>Blog</li><li>Articles</li></ul>

    <div class="f-brand"><i></i>Velnik Mobility</div>
    <p class="f-copy">© 2023 Velnik Inc. All rights reserved.</p>

    <span class="f-label" style="left:324px;top:232px">Get in Touch</span>
    <ul class="f-list" style="left:324px;top:250px"><li>info@velnik.com</li><li>+1 555 014 2278</li></ul>
    <span class="f-label" style="left:461px;top:232px">Subscribe to Stay Notified</span>
    <div class="f-input">Enter Your Email Address</div>
    <div class="f-send"><svg width="12" height="12" viewBox="0 0 12 12"><path d="M1 6L11 1L7.5 11L6 7Z" fill="#101010"/></svg></div>

    <div class="f-rule"></div>
    <ul class="f-legal"><li>Cookie policy</li><li>Terms &amp; Conditions</li><li>Privacy Policy</li></ul>
    <p class="f-note">Velnik is an e-mobility service provider with a comprehensive digital platform and is not a direct transportation service provider. All e-mobility services and vehicles offered through Velnik are provided by licensed and reputable third-party providers, fully compliant with relevant regulatory authorities, including those established by regional and national bodies.</p>
  </footer>

</main>
</body>
</html>
```